Saucy Velvet Impz Business Card

We need business cards designed for our consultants to use and hand out to customers.
We are an Adult party plan company (like Crelvaware but sex toys and lingerie)
We would like bright colours pinks, purples.
The cards need our logo
Space for the reps phone number email address and name.
We need our website on it www.saucyvelvetimps.com.au

```html
<!DOCTYPE html>
<html lang="en">
<head>
<meta charset="utf-8">
<title>Saucy Velvet Impz – Business Card Options</title>
<link href="https://fonts.googleapis.com/css2?family=Arimo:wght@400&display=swap" rel="stylesheet">
<style>
  :root {
    --canvas-bg: #ffffff;
    --velvet-glow: #6b2f92;
    --velvet-mid: #4e1f6c;
    --velvet-deep: #33114a;
    --night-glow: #3a1a4a;
    --night-deep: #140816;
    --ink-light: #ffffff;
    --ink-soft: rgba(255, 255, 255, 0.82);
    --ink-faint: #a678c8;
    --rule-soft: rgba(255, 255, 255, 0.35);
  }
  * { margin: 0; padding: 0; box-sizing: border-box; }
  html, body {
    width: 1200px;
    height: 692px;
    overflow: hidden;
    background: var(--canvas-bg);
  }
  .sheet {
    position: relative;
    width: 1200px;
    height: 692px;
    font-family: "Arimo", Helvetica, Arial, sans-serif;
  }
  .card {
    position: absolute;
    top: 54px;
    width: 362px;
    height: 587px;
    overflow: hidden;
  }
  .card--plain {
    background: radial-gradient(ellipse 75% 60% at 62% 50%, var(--velvet-glow) 0%, var(--velvet-mid) 55%, var(--velvet-deep) 100%);
  }
  .card--patterned {
    background: radial-gradient(ellipse 80% 70% at 65% 55%, var(--night-glow) 0%, #24102c 55%, var(--night-deep) 100%);
  }
  .card--faint {
    background: radial-gradient(ellipse 75% 60% at 40% 55%, var(--velvet-glow) 0%, var(--velvet-mid) 55%, var(--velvet-deep) 100%);
  }
  .card--left   { left: 36px; }
  .card--centre { left: 420px; width: 361px; }
  .card--right  { left: 804px; }

  .card__pattern {
    position: absolute;
    inset: 0;
    background: radial-gradient(circle at 70% 40%, rgba(120, 70, 150, 0.35) 0%, rgba(60, 25, 70, 0.15) 45%, transparent 75%);
  }
  .card__brand {
    position: absolute;
    left: 0;
    right: 0;
    top: 262px;
    text-align: center;
    font-size: 34px;
    font-weight: 400;
    line-height: 1.2;
    color: var(--ink-light);
  }
  .card--faint .card__brand { color: var(--ink-faint); }

  .card__rep {
    position: absolute;
    left: 70px;
    right: 70px;
    top: 360px;
    list-style: none;
    font-size: 13px;
    line-height: 1;
    color: var(--ink-soft);
  }
  .card__rep-field {
    display: flex;
    align-items: flex-end;
    gap: 8px;
    height: 26px;
  }
  .card__rep-label { width: 44px; flex: none; }
  .card__rep-line {
    flex: 1;
    border-bottom: 1px solid var(--rule-soft);
    margin-bottom: 2px;
  }

  .card__web {
    position: absolute;
    left: 0;
    right: 0;
    top: 476px;
    text-align: center;
    font-size: 19.5px;
    color: var(--ink-light);
    letter-spacing: 0.1px;
  }
</style>
</head>
<body>
<main class="sheet">
  <section class="card card--plain card--left">
    <p class="card__brand">Saucy Velvet Impz</p>
    <ul class="card__rep">
      <li class="card__rep-field"><span class="card__rep-label">Name</span><span class="card__rep-line"></span></li>
      <li class="card__rep-field"><span class="card__rep-label">Phone</span><span class="card__rep-line"></span></li>
      <li class="card__rep-field"><span class="card__rep-label">Email</span><span class="card__rep-line"></span></li>
    </ul>
    <p class="card__web">www.saucyvelvetimps.com.au</p>
  </section>

  <section class="card card--patterned card--centre">
    <div class="card__pattern" role="img" aria-label="Dark purple paisley pattern background"></div>
    <p class="card__brand">Saucy Velvet Impz</p>
    <ul class="card__rep">
      <li class="card__rep-field"><span class="card__rep-label">Name</span><span class="card__rep-line"></span></li>
      <li class="card__rep-field"><span class="card__rep-label">Phone</span><span class="card__rep-line"></span></li>
      <li class="card__rep-field"><span class="card__rep-label">Email</span><span class="card__rep-line"></span></li>
    </ul>
    <p class="card__web">www.saucyvelvetimps.com.au</p>
  </section>

  <section class="card card--faint card--right">
    <p class="card__brand">Saucy Velvet Impz</p>
    <ul class="card__rep">
      <li class="card__rep-field"><span class="card__rep-label">Name</span><span class="card__rep-line"></span></li>
      <li class="card__rep-field"><span class="card__rep-label">Phone</span><span class="card__rep-line"></span></li>
      <li class="card__rep-field"><span class="card__rep-label">Email</span><span class="card__rep-line"></span></li>
    </ul>
    <p class="card__web">www.saucyvelvetimps.com.au</p>
  </section>
</main>
</body>
</html>
```